Business Card Design for a Personal Trainer

I need a business card design for my job as a personal trainer. It should have a unique, modern and exclusive design. On the front there should be only my logo with my name and my job. 0163/2918374 Tobias Kellinger Lindenfeldweg 14 80412 Munich Germany The most important contact information is the web adress. it can be bigger than the rest, but its not necessary. The card should be 8,5cmx5,5cm big. Font: Roboto. Colors: black, white, gray, 56c1ff.

```html
<!DOCTYPE html>
<html lang="de">
<head>
<meta charset="utf-8">
<title>Tobias Kellinger – Personal Trainer Business Card</title>
<link rel="stylesheet" href="https://fonts.googleapis.com/css2?family=Roboto:wght@400;500;700&display=swap">
<style>
  :root {
    --page-bg: #d7dadd;
    --card-bg: #1c1719;
    --card-bg-soft: #2a2427;
    --accent: #56c1ff;
    --white: #ffffff;
    --gray: #a9a9ad;
    --photo-light: #8d8d90;
    --photo-dark: #2e2e30;
  }
  * { box-sizing: border-box; margin: 0; padding: 0; }
  html, body {
    width: 1200px;
    height: 900px;
    overflow: hidden;
    background: var(--page-bg);
    font-family: "Roboto", Arial, sans-serif;
  }
  .card {
    position: absolute;
    left: 320px;
    width: 560px;
    height: 362px;
    border-radius: 22px;
    background: var(--card-bg);
    overflow: hidden;
    box-shadow: 0 14px 30px rgba(0,0,0,0.28);
  }
  .card--front { top: 58px; }
  .card--back  { top: 480px; }

  .dot-texture {
    position: absolute;
    right: 0;
    top: 0;
    width: 62%;
    height: 100%;
    background: linear-gradient(200deg, var(--card-bg-soft) 0%, var(--card-bg) 80%);
  }

  /* front */
  .brand {
    position: absolute;
    left: 34px;
    top: 34px;
    display: flex;
    align-items: center;
    gap: 10px;
  }
  .brand__square {
    width: 22px;
    height: 22px;
    background: var(--gray);
  }
  .brand__name {
    color: var(--gray);
    font-size: 15px;
    font-weight: 500;
    letter-spacing: 1.5px;
  }
  .name-frame {
    position: absolute;
    left: 250px;
    top: 140px;
    width: 230px;
    height: 150px;
  }
  .name-frame svg { position: absolute; inset: 0; }
  .name-frame__name {
    position: absolute;
    left: 22px;
    top: 28px;
    color: var(--accent);
    font-size: 25px;
    font-weight: 700;
    white-space: nowrap;
  }
  .name-frame__role {
    position: absolute;
    left: 22px;
    top: 62px;
    color: var(--white);
    font-size: 14px;
    letter-spacing: 2px;
  }

  /* back */
  .portrait {
    position: absolute;
    left: 40px;
    top: 34px;
    width: 170px;
    height: 170px;
    border-radius: 50%;
    border: 6px solid var(--accent);
    background: radial-gradient(circle at 50% 40%, var(--photo-light), var(--photo-dark) 75%);
  }
  .website {
    position: absolute;
    left: 30px;
    bottom: 44px;
    color: var(--white);
    font-size: 24px;
    font-weight: 700;
    white-space: nowrap;
  }
  .contact-frame {
    position: absolute;
    left: 318px;
    top: 66px;
    width: 222px;
    height: 230px;
  }
  .contact-frame svg.frame { position: absolute; inset: 0; }
  .contact-list {
    position: absolute;
    left: 20px;
    top: 50px;
    list-style: none;
    color: var(--white);
    font-size: 12.5px;
    letter-spacing: 0.8px;
    line-height: 22px;
    white-space: nowrap;
  }
  .contact-list li { display: flex; align-items: flex-start; gap: 9px; }
  .contact-list svg { flex: none; margin-top: 5px; }
</style>
</head>
<body>

<section class="card card--front">
  <div class="dot-texture" role="img" aria-label="Subtle gray halftone dot texture"></div>
  <div class="brand">
    <span class="brand__square"></span>
    <span class="brand__name">TOBIAS KELLINGER</span>
  </div>
  <div class="name-frame">
    <svg width="230" height="150" viewBox="0 0 230 150" aria-hidden="true">
      <polyline points="120,3 3,3 3,147 200,147" fill="none" stroke="#56c1ff" stroke-width="5"/>
    </svg>
    <div class="name-frame__name">Tobias Kellinger</div>
    <div class="name-frame__role">Personal Trainer</div>
  </div>
</section>

<section class="card card--back">
  <div class="dot-texture" role="img" aria-label="Subtle gray halftone dot texture"></div>
  <div class="portrait" role="img" aria-label="Black and white portrait photo of the trainer"></div>
  <div class="website">www.tobiaskellinger.de</div>
  <div class="contact-frame">
    <svg class="frame" width="222" height="230" viewBox="0 0 222 230" aria-hidden="true">
      <polyline points="130,3 3,3 3,227 219,227" fill="none" stroke="#56c1ff" stroke-width="5"/>
    </svg>
    <ul class="contact-list">
      <li>
        <svg width="12" height="10" viewBox="0 0 12 10" aria-hidden="true"><rect x="0.5" y="0.5" width="11" height="9" fill="none" stroke="#56c1ff"/><polyline points="0.5,0.5 6,5 11.5,0.5" fill="none" stroke="#56c1ff"/></svg>
        <span>t.kellinger@postfeld.de</span>
      </li>
      <li>
        <svg width="12" height="12" viewBox="0 0 12 12" aria-hidden="true"><path d="M2 1 L4.5 1 L5.5 3.5 L4 4.7 Q5 7 7.3 8 L8.5 6.5 L11 7.5 L11 10 Q6 11 3 7.5 Q1 5 2 1Z" fill="#56c1ff"/></svg>
        <span>0163/2918374</span>
      </li>
      <li>
        <svg width="12" height="12" viewBox="0 0 12 12" aria-hidden="true"><path d="M6 11 Q1.5 6 1.5 4.5 A4.5 4.5 0 0 1 10.5 4.5 Q10.5 6 6 11Z" fill="#56c1ff"/><circle cx="6" cy="4.5" r="1.6" fill="#1c1719"/></svg>
        <span>Lindenfeldweg 14<br>80412 München</span>
      </li>
    </ul>
  </div>
</section>

</body>
</html>
```